Power point Presentation Template 2

I am looking a professionally designed Powerpoint Presentation template for my company. We are Information Technology Company. I have attached the Logo. The Logo will also give an indication of which colours to be used in the design.

Information and Communication Technology

• All ideas welcomed
• Professional Look and Feel

```html
<!DOCTYPE html>
<html lang="en">
<head>
<meta charset="utf-8">
<title>Presentation Template – Slide Set</title>
<link rel="stylesheet" href="https://fonts.googleapis.com/css2?family=Barlow+Condensed:wght@500&family=Barlow+Semi+Condensed:wght@400&family=Nunito+Sans:wght@400&display=swap">
<style>
  :root {
    --canvas-bg: #d9d6d3;
    --slide-dark: #242424;
    --slide-light: #ffffff;
    --accent-blue: #2d9fdb;
    --accent-orange: #f7941d;
    --text-light: #d4d4d4;
    --text-body: #555555;
    --rule-dark: #8a8a8a;
    --rule-light: #b5b5b5;
  }
  * { box-sizing: border-box; margin: 0; padding: 0; }
  html, body { width: 1200px; height: 870px; overflow: hidden; }
  body { background: var(--canvas-bg); position: relative; }

  .slide {
    position: absolute;
    width: 560px;
    height: 315px;
    overflow: hidden;
    background: var(--slide-dark);
    box-shadow: 0 2px 8px rgba(0,0,0,0.25);
  }
  .slide--title   { left: 40px;  top: 34px; }
  .slide--section { left: 600px; top: 102px; }
  .slide--split   { left: 40px;  top: 418px; }
  .slide--content { left: 600px; top: 518px; background: var(--slide-light); }

  .kicker {
    position: absolute;
    font-family: "Barlow Semi Condensed", sans-serif;
    font-weight: 400;
    color: var(--text-light);
    text-transform: uppercase;
    line-height: 1;
    white-space: nowrap;
  }
  .rule { position: absolute; height: 1px; background: var(--rule-dark); }
  .headline {
    position: absolute;
    font-family: "Barlow Condensed", sans-serif;
    font-weight: 500;
    color: var(--accent-blue);
    text-transform: uppercase;
    line-height: 1;
    white-space: nowrap;
    letter-spacing: -0.5px;
  }

  /* Title slide */
  .brand {
    position: absolute;
    left: 166px; top: 50px;
    display: flex; align-items: center; gap: 10px;
    color: var(--accent-orange);
    font-family: "Barlow Condensed", sans-serif;
    font-weight: 500;
  }
  .brand__dot { width: 40px; height: 40px; border-radius: 50%; background: var(--accent-orange); }
  .brand__name { font-size: 44px; line-height: 0.9; letter-spacing: 1px; }
  .brand__tag { display: block; font-size: 12px; letter-spacing: 6px; line-height: 1.2; }
  .slide--title .kicker { left: 22px; top: 172px; font-size: 21px; }
  .slide--title .rule { left: 22px; top: 198px; width: 517px; }
  .slide--title .headline { left: 22px; top: 200px; font-size: 64px; }

  /* Section slide */
  .section-photo {
    position: absolute; inset: 0;
    background: linear-gradient(120deg, #3c3c3c 0%, #555 45%, #7a7a7a 62%, #444 75%, #2e2e2e 100%);
  }
  .slide--section .kicker { left: 20px; top: 174px; font-size: 20px; color: #e2e2e2; }
  .slide--section .rule { left: 20px; top: 199px; width: 522px; background: #9a9a9a; }
  .slide--section .headline { left: 20px; top: 204px; font-size: 52px; }

  /* Split slide */
  .split-photo {
    position: absolute; left: 70px; top: 0; width: 176px; height: 315px;
    background: linear-gradient(180deg, #6e6e6e 0%, #b9b9b9 40%, #e2e2e2 75%, #cfcfcf 100%);
  }
  .slide--split .kicker { left: 262px; top: 151px; font-size: 20px; line-height: 21px; }
  .slide--split .rule { left: 262px; top: 199px; width: 216px; }
  .slide--split .headline { left: 262px; top: 204px; font-size: 32px; line-height: 33px; }

  /* Content slide */
  .slide--content .kicker { left: 85px; top: 18px; font-size: 9px; color: #555; letter-spacing: 0.4px; }
  .slide--content .rule { left: 85px; top: 32px; width: 392px; background: var(--rule-light); }
  .slide--content .headline { left: 85px; top: 49px; font-size: 18px; letter-spacing: 0; }
  .bullets {
    position: absolute; left: 85px; top: 90px; width: 345px;
    list-style: none;
    font-family: "Nunito Sans", sans-serif;
    font-size: 13.5px; line-height: 18px; color: var(--text-body);
  }
  .bullets li { position: relative; padding-left: 13px; margin-bottom: 12px; }
  .bullets svg { position: absolute; left: 3px; top: 5px; }
</style>
</head>
<body>

<section class="slide slide--title">
  <div class="brand">
    <span class="brand__dot"></span>
    <span class="brand__name">NOVARIS<span class="brand__tag">TECHNOLOGIES</span></span>
  </div>
  <p class="kicker">Lorem ipsum dolor sit amet</p>
  <div class="rule"></div>
  <h1 class="headline">Etiam tempor orci eu</h1>
</section>

<section class="slide slide--section">
  <div class="section-photo" role="img" aria-label="Black and white photo of a curved concrete dam wall with a walkway along its top"></div>
  <p class="kicker">Nibh tellus molestie</p>
  <div class="rule"></div>
  <h2 class="headline">Porta nibh venenatis cras</h2>
</section>

<section class="slide slide--split">
  <div class="split-photo" role="img" aria-label="Black and white photo of wind turbines against a cloudy sky"></div>
  <p class="kicker">Aliquam ultrices<br>sagittis orci a</p>
  <div class="rule"></div>
  <h2 class="headline">Dignissim diam<br>quis enim lobortis</h2>
</section>

<section class="slide slide--content">
  <p class="kicker">Elementum nibh tellus</p>
  <div class="rule"></div>
  <h2 class="headline">Volutpat commodo sed egestas</h2>
  <ul class="bullets">
    <li><svg width="5" height="8" viewBox="0 0 5 8"><path d="M0 0L5 4L0 8Z" fill="#2d9fdb"/></svg>Etiam tempor orci eu lobortis elementum nibh tellus molestie.</li>
    <li><svg width="5" height="8" viewBox="0 0 5 8"><path d="M0 0L5 4L0 8Z" fill="#2d9fdb"/></svg>Neque egestas congue quisque egestas.</li>
    <li><svg width="5" height="8" viewBox="0 0 5 8"><path d="M0 0L5 4L0 8Z" fill="#2d9fdb"/></svg>Egestas integer eget aliquet nibh praesent tristique.</li>
    <li><svg width="5" height="8" viewBox="0 0 5 8"><path d="M0 0L5 4L0 8Z" fill="#2d9fdb"/></svg>Vulputate mi sit amet mauris.</li>
    <li><svg width="5" height="8" viewBox="0 0 5 8"><path d="M0 0L5 4L0 8Z" fill="#2d9fdb"/></svg>Sodales neque sodales ut etiam sit.</li>
  </ul>
</section>

</body>
</html>
```